Now Open Poster

We need a banner for our sports supplement and nutritional store, Harbor Nutrition.
We were hoping for some sort of creative word art piece.
I have drawn my own mock up just to give you all a very basic starting point. But you are free to go with whatever you feel will work best.
The primary objective is simply to explain a little about what the company does, and then direct traffic towards the store with an 'Open Arrow' pointing left.
Text words we have chosen are:
Protein
Creatine
Health
Fitness
Sports Science
Nutrition
Energy
Achievement
Amino Acids
Organic
Supplements
Performance
Testosterone Support
Vitamins
Growth
Diet
Happiness
Weight Loss
Strong
Natural
Vitality
Accomplished
Below the word art we want our logo (See attached options)
Then below the logo the phrase "Success Starts Here"
Dimensions of the poster are 140cm x 60cm.
Colours: Blues/Whites/Greys/Blacks (Lots of white space please)
Here are some cool pieces I found that had some interesting elements that I liked (I'd love to see a mash-up of styles with a street art feel to it. Something funky!):
http://www.moodwall-example.com/pin/100000000000000001/
http://www.moodwall-example.com/pin/100000000000000002/
http://www.moodwall-example.com/pin/100000000000000003/
http://www.moodwall-example.com/pin/100000000000000004/
http://www.moodwall-example.com/pin/100000000000000005/
Thanks for reading, message me if you have any further questions!
- Tobias

```html
<!DOCTYPE html>
<html lang="en">
<head>
<meta charset="utf-8">
<title>Harbor Nutrition – Now Open</title>
<link rel="stylesheet" href="https://fonts.googleapis.com/css2?family=Oswald:wght@400;500;700&family=Questrial&family=Josefin+Sans:wght@200;300&family=Share+Tech+Mono&display=swap">
<style>
  :root {
    --paper: #ffffff;
    --ink: #111111;
    --sky: #1ba8ec;
    --stone: #8e8e8e;
  }
  html, body {
    margin: 0;
    padding: 0;
    width: 1200px;
    height: 2801px;
    overflow: hidden;
    background: var(--paper);
  }
  .poster {
    display: block;
    width: 1200px;
    height: 2801px;
    background: var(--paper);
  }
  .word { text-transform: uppercase; }
  .ink   { fill: var(--ink); }
  .sky   { fill: var(--sky); }
  .stone { fill: var(--stone); }

  .condensed      { font-family: "Oswald", "Arial Narrow", sans-serif; font-weight: 700; }
  .condensed-mid  { font-family: "Oswald", "Arial Narrow", sans-serif; font-weight: 500; }
  .condensed-reg  { font-family: "Oswald", "Arial Narrow", sans-serif; font-weight: 400; }
  .geometric      { font-family: "Questrial", "Century Gothic", sans-serif; }
  .hairline       { font-family: "Josefin Sans", "Century Gothic", sans-serif; font-weight: 200; }
  .mono           { font-family: "Share Tech Mono", "Lucida Console", monospace; }

  .seal-ring { fill: none; stroke: var(--ink); stroke-width: 2.4; }
</style>
</head>
<body>
<svg class="poster" viewBox="0 0 556 1298" width="1200" height="2801" xmlns="http://www.w3.org/2000/svg" role="img" aria-label="Harbor Nutrition now open poster">
  <!-- Headline: open arrows pointing left -->
  <text class="open-sign geometric ink" x="68" y="88" font-size="64" textLength="422" lengthAdjust="spacingAndGlyphs">« « Open « «</text>

  <!-- Word art -->
  <text class="word condensed sky"   x="35"  y="185" font-size="82" textLength="233" lengthAdjust="spacingAndGlyphs">Health</text>
  <text class="word geometric ink"   x="338" y="155" font-size="47" textLength="184" lengthAdjust="spacingAndGlyphs">Protein</text>
  <text class="word geometric ink"   x="335" y="205" font-size="47" textLength="187" lengthAdjust="spacingAndGlyphs">Creatine</text>

  <text class="word hairline ink"    x="35"  y="300" font-size="116" textLength="487" lengthAdjust="spacingAndGlyphs">Fitness</text>
  <text class="word mono stone"      x="35"  y="355" font-size="57" textLength="485" lengthAdjust="spacingAndGlyphs">Sports Science</text>

  <text class="word geometric ink"   x="35"  y="400" font-size="32" textLength="168" lengthAdjust="spacingAndGlyphs">Nutrition</text>
  <text class="word geometric sky"   x="35"  y="448" font-size="43" textLength="165" lengthAdjust="spacingAndGlyphs">Energy</text>
  <text class="word condensed ink"   x="207" y="448" font-size="100" textLength="315" lengthAdjust="spacingAndGlyphs">Achievement</text>

  <text class="word geometric ink"   x="35"  y="497" font-size="47" textLength="287" lengthAdjust="spacingAndGlyphs">Suppliments</text>
  <text class="word geometric ink"   x="335" y="497" font-size="40" textLength="185" lengthAdjust="spacingAndGlyphs">Organic</text>

  <text class="word geometric ink"   x="35"  y="548" font-size="40" textLength="235" lengthAdjust="spacingAndGlyphs">Amino Acids</text>
  <text class="word condensed-mid sky" x="278" y="545" font-size="48" textLength="244" lengthAdjust="spacingAndGlyphs">Performance</text>

  <text class="word mono sky"        x="38"  y="590" font-size="46" textLength="484" lengthAdjust="spacingAndGlyphs">Tetosterone Support</text>

  <text class="word mono stone"      x="35"  y="638" font-size="50" textLength="245" lengthAdjust="spacingAndGlyphs">Vitamins</text>
  <text class="word condensed ink"   x="283" y="665" font-size="75" textLength="239" lengthAdjust="spacingAndGlyphs">Growth</text>
  <text class="word geometric ink"   x="35"  y="665" font-size="29" textLength="60" lengthAdjust="spacingAndGlyphs">Diet</text>
  <text class="word condensed-mid ink" x="140" y="665" font-size="25" textLength="130" lengthAdjust="spacingAndGlyphs">Weight Loss</text>

  <text class="word hairline sky"    x="35"  y="738" font-size="88" textLength="487" lengthAdjust="spacingAndGlyphs">Happiness</text>
  <text class="word mono stone"      x="35"  y="805" font-size="79" textLength="487" lengthAdjust="spacingAndGlyphs">I am Strong</text>

  <text class="word geometric sky"   x="35"  y="852" font-size="50" textLength="230" lengthAdjust="spacingAndGlyphs">Natural</text>
  <text class="word mono ink"        x="270" y="850" font-size="50" textLength="252" lengthAdjust="spacingAndGlyphs">Vitality</text>

  <text class="word geometric stone" x="35"  y="905" font-size="64" textLength="487" lengthAdjust="spacingAndGlyphs">Accomplished</text>

  <text class="word condensed-reg ink" x="35" y="1018" font-size="118" textLength="487" lengthAdjust="spacingAndGlyphs">I am King</text>

  <!-- Brand seal -->
  <g class="brand-seal">
    <circle class="seal-ring" cx="278" cy="1108" r="78"/>
    <text class="word geometric ink" x="278" y="1114" font-size="17" text-anchor="middle" textLength="118" lengthAdjust="spacingAndGlyphs">Harbor Nutrition</text>
  </g>

  <!-- Tagline -->
  <text class="word mono ink" x="35" y="1262" font-size="43" textLength="483" lengthAdjust="spacingAndGlyphs">Success Starts Here!</text>
</svg>
</body>
</html>
```